Rapid Lap Raceway Belmore group booking promotion

-A flyer that entitles potential customers $100 off our exclusive hire group booking
-Bookings are for groups of 10 or more
-Voucher is only redeemable for exclusive hire and must be booked in advanced (not walk-in)
-Must have a blank space where we can put the person’s/business’ name (to: [blank] and the expiry date (must book before: [blank])
-Targeted at other businesses and sporting groups (organisations that have more than 10 people) as a team building activity or celebratory activity
-Flyers will either be delivered personally or to their mailbox
-Contact details: ph 9267 5813, website rapidlap.com.au, email info@rapidlap.com.au
-must have the go-kart logo
-attached is some previous advertising material

Target Market(s)

Businesses, sporting groups, organisations

Industry/Entity Type

Advertising

Font styles to use
Sans Serif

Requirements
Must have
• go kart logo, gift voucher layout, "$100 off" very bold and clear, spaces to write "to:" and "must book before:", our phone number and website,
• MAKE THESE THINGS STAND OUT AND KEEP OTHER INFORMATION TO A MINIMUM.
Nice to have
• Quotes that promote go-karting as an exercise for team-building, state that voucher is only redeemable for exclusive hire
Should not have
• Information on pricing (let the customer make contact via website or directly to get more information)

```html
<!DOCTYPE html>
<html lang="en">
<head>
<meta charset="utf-8">
<title>Rapid Lap Raceway Belmore – Group Booking Voucher</title>
<link rel="stylesheet" href="https://fonts.googleapis.com/css2?family=Open+Sans:wght@400;600;700;800&family=Great+Vibes&display=swap">
<style>
  :root {
    --backdrop: #ece4d8;
    --flyer-yellow: #fcd23c;
    --flyer-yellow-deep: #f5b923;
    --race-red: #e2392b;
    --ink: #151515;
    --white: #ffffff;
    --voucher-cream: #fbecb0;
    --voucher-line: #9b8f70;
    --check-light: #e8e8e8;
    --check-dark: #1c1c1c;
  }
  * { box-sizing: border-box; margin: 0; padding: 0; }
  html, body { width: 992px; height: 1200px; overflow: hidden; }
  body {
    background: var(--backdrop);
    font-family: "Open Sans", Arial, sans-serif;
    color: var(--ink);
    position: relative;
  }
  .flyer {
    position: absolute;
    left: 16px; top: 365px;
    width: 960px; height: 470px;
    display: flex;
    box-shadow: 0 6px 18px rgba(0,0,0,.18);
  }

  /* ---------- promotion panel ---------- */
  .promo {
    position: relative;
    width: 500px; height: 470px;
    background: var(--flyer-yellow);
    overflow: hidden;
  }
  .promo-shapes { position: absolute; inset: 0; }
  .checker-band { position: absolute; inset: 0; }
  .discount-burst {
    position: absolute; left: 12px; top: 22px;
    width: 160px; height: 160px;
  }
  .discount-burst__text {
    position: absolute; inset: 0;
    display: flex; flex-direction: column; align-items: center; justify-content: center;
    color: var(--white); font-weight: 800; line-height: 1;
    transform: rotate(-12deg);
  }
  .discount-burst__amount { font-size: 44px; }
  .discount-burst__off { font-size: 20px; color: var(--ink); align-self: flex-end; margin-right: 28px; }

  .brand-name {
    position: absolute; left: 182px; top: 20px; width: 310px;
    font-size: 38px; font-weight: 800; line-height: 1.0;
    color: var(--ink); text-transform: uppercase; letter-spacing: -0.5px;
  }

  .offer {
    position: absolute; left: 20px; top: 222px; width: 320px;
  }
  .offer__lead { font-size: 17px; font-weight: 800; line-height: 1.2; }
  .offer__lead em { font-style: normal; color: var(--race-red); }
  .offer__group { font-size: 25px; font-weight: 800; line-height: 1.15; }
  .offer__group em { font-style: normal; color: var(--race-red); }
  .offer__audience { margin-top: 4px; font-size: 14px; font-weight: 600; line-height: 1.2; }
  .offer__note { font-size: 10.5px; font-weight: 400; }
  .offer__purpose { font-size: 13px; font-weight: 800; line-height: 1.2; }

  .contact {
    position: absolute; right: 14px; top: 150px; width: 230px; text-align: right;
  }
  .contact__hint { font-size: 9.5px; line-height: 1.25; }
  .contact__phone { font-size: 26px; font-weight: 800; color: var(--race-red); line-height: 1.15; }
  .contact__email { font-size: 11px; font-weight: 700; }

  .kart-art {
    position: absolute; left: 338px; top: 228px;
    width: 150px; height: 140px; border-radius: 14px;
    background: radial-gradient(circle at 45% 45%, #d8423a 0%, #b8312b 45%, #3a5ea8 75%, rgba(40,40,40,.6) 100%);
  }
  .site-url {
    position: absolute; left: 22px; bottom: 16px;
    font-size: 33px; font-weight: 800; color: var(--white); letter-spacing: 0.3px;
  }

  /* ---------- voucher ---------- */
  .voucher {
    position: relative;
    width: 460px; height: 470px;
    background: var(--voucher-cream);
    border-left: 2px dashed var(--ink);
  }
  .scissors { position: absolute; left: -12px; top: 8px; width: 22px; height: 22px; background: var(--voucher-cream); }
  .voucher__frame {
    position: absolute; inset: 14px;
    border: 9px double var(--race-red);
  }
  .voucher__title {
    position: absolute; left: 40px; top: 44px;
    font-family: "Great Vibes", cursive; font-size: 52px; color: var(--race-red); line-height: 1;
  }
  .voucher__brand {
    position: absolute; right: 40px; top: 40px; width: 200px; text-align: right;
    font-size: 20px; font-weight: 800; line-height: 1.05; text-transform: uppercase;
  }
  .voucher__badge {
    position: absolute; right: 44px; top: 112px;
    width: 92px; height: 92px; border-radius: 50%;
    background: radial-gradient(circle, #f7c98f 0%, #f4b780 60%, rgba(244,183,128,0) 100%);
    display: flex; flex-direction: column; align-items: center; justify-content: center;
    line-height: 1;
  }
  .voucher__badge-amount { font-size: 28px; font-weight: 800; color: var(--race-red); }
  .voucher__badge-off { font-size: 22px; font-weight: 600; color: var(--ink); }
  .voucher__fields { position: absolute; left: 40px; top: 150px; width: 260px; }
  .field { display: flex; align-items: flex-end; gap: 8px; height: 34px; font-size: 12px; }
  .field__line { flex: 1; border-bottom: 1px solid var(--voucher-line); height: 1px; margin-bottom: 3px; }
  .signature {
    position: absolute; right: 40px; top: 262px; width: 150px;
    border-top: 1px solid var(--voucher-line); padding-top: 3px;
    font-size: 10px; text-align: right;
  }
  .festive-art {
    position: absolute; left: 40px; bottom: 40px;
    width: 150px; height: 120px; border-radius: 10px;
    background: radial-gradient(circle at 40% 50%, #f6b394 0%, rgba(246,179,148,.45) 55%, rgba(246,179,148,0) 100%);
  }
  .voucher__terms {
    position: absolute; left: 200px; right: 40px; bottom: 46px;
    font-size: 11.5px; font-weight: 700; line-height: 1.35;
  }
</style>
</head>
<body>
  <main class="flyer">
    <section class="promo">
      <svg class="promo-shapes" viewBox="0 0 500 470" aria-hidden="true">
        <path d="M0 430 C 160 400 340 360 500 330 L500 470 L0 470 Z" fill="var(--race-red)"/>
        <path d="M0 444 C 160 414 340 378 500 350 L500 470 L0 470 Z" fill="var(--ink)"/>
      </svg>
      <svg class="checker-band" viewBox="0 0 500 470" role="img" aria-label="Chequered racing flag band">
        <defs>
          <linearGradient id="checkerTone" x1="0" y1="0" x2="1" y2="0">
            <stop offset="0" stop-color="var(--check-dark)"/>
            <stop offset="0.5" stop-color="#7a7a7a"/>
            <stop offset="1" stop-color="var(--check-dark)"/>
          </linearGradient>
        </defs>
        <polygon points="0,188 500,98 500,124 0,214" fill="url(#checkerTone)"/>
      </svg>

      <div class="discount-burst">
        <svg viewBox="0 0 160 160" width="160" height="160" aria-hidden="true">
          <polygon fill="var(--race-red)" points="80,2 90,20 106,6 111,26 130,18 128,39 150,37 140,56 158,66 142,80 158,94 140,104 150,123 128,121 130,142 111,134 106,154 90,140 80,158 70,140 54,154 49,134 30,142 32,121 10,123 20,104 2,94 18,80 2,66 20,56 10,37 32,39 30,18 49,26 54,6 70,20"/>
        </svg>
        <div class="discount-burst__text">
          <span class="discount-burst__amount">$100</span>
          <span class="discount-burst__off">OFF</span>
        </div>
      </div>

      <h1 class="brand-name">Rapid Lap Raceway Belmore</h1>

      <div class="contact">
        <p class="contact__hint">If you require any further information or<br>wish to make a booking please phone us on:</p>
        <p class="contact__phone">Ph. 9267 5813</p>
        <p class="contact__email">email info@rapidlap.com.au</p>
      </div>

      <div class="offer">
        <p class="offer__lead">Our <em>Exclusive Hire Group</em> Bookings are for</p>
        <p class="offer__group">groups of <em>10</em> or more</p>
        <p class="offer__audience">Businesses and Sporting groups</p>
        <p class="offer__note">(organisations that have more than 10 people)</p>
        <p class="offer__purpose">as a team building activity<br>or celebratory activity</p>
      </div>

      <div class="kart-art" role="img" aria-label="Illustration of a helmeted driver racing a red go-kart"></div>

      <p class="site-url">www.rapidlap.com.au</p>
    </section>

    <section class="voucher">
      <svg class="scissors" viewBox="0 0 22 22" aria-hidden="true">
        <circle cx="6" cy="6" r="3.2" fill="none" stroke="var(--ink)" stroke-width="1.6"/>
        <circle cx="6" cy="16" r="3.2" fill="none" stroke="var(--ink)" stroke-width="1.6"/>
        <path d="M8.5 7.5 L20 15 M8.5 14.5 L20 7" stroke="var(--ink)" stroke-width="1.6"/>
      </svg>
      <div class="voucher__frame"></div>

      <p class="voucher__title">Gift Voucher</p>
      <p class="voucher__brand">Rapid Lap Raceway Belmore</p>
      <div class="voucher__badge">
        <span class="voucher__badge-amount">$100</span>
        <span class="voucher__badge-off">off</span>
      </div>

      <div class="voucher__fields">
        <div class="field"><span>Name</span><span class="field__line"></span></div>
        <div class="field"><span>Address</span><span class="field__line"></span></div>
        <div class="field"><span class="field__line"></span></div>
        <div class="field"><span>Expiry Date</span><span class="field__line"></span></div>
      </div>
      <p class="signature">Authorised Signature</p>

      <div class="festive-art" role="img" aria-label="Christmas stocking and snowflake decoration"></div>
      <p class="voucher__terms">Voucher is only redeemable for exclusive hire and must be booked in advanced (not walk-in)</p>
    </section>
  </main>
</body>
</html>
```